New flyer design for construction company marketing and description of services.

I want to have a flyer design that my techs will carry to deliver after job completion or for marketing purposes, to explain what services we provide, we offer General construction services.

Brightnail Handyman Sevices originated from a family-owned and operated contractor business, performing home renovation, addition, and construction work in the NYC area since 2004.

Today, we specialize in reliable and affordable Construction services for residential and commercial clients In 2014, we expanded to northern New Jersey. In 2016, we brought quality home improvement and repair services to new Bucks County, PA, and nearby New Jersey areas.
We offer carpentry, electrical, plumbing, renovation, remodel, cleaning services and landscaping.
I would like to have a section for home rental maintenance.

Target Market(s)

Homeowners, rental properties, real state and Senior citizen

Industry/Entity Type

Construction Company

Colors

Designer to choose colors to be used in the design.

Requirements
Must have
• A special design that will attract 55 + clients maybe a logo version that will be more attractive to seniors. I would updated the briefing with design and previous pictures, but we have all available in our social media instagram and facebook:
• https://www.sampleinsta.test/brightnailhandyman/?hl=en
• https://www.samplefacebook.test/brightnailhandy/
Nice to have
• New design ideas and layouts.

```html
<!DOCTYPE html>
<html lang="en">
<head>
<meta charset="UTF-8">
<title>Brightnail Handyman Services Flyer</title>
<link href="https://fonts.googleapis.com/css2?family=Archivo+Black&family=Roboto+Condensed:wght@700&family=Roboto:wght@400;700;900&display=swap" rel="stylesheet">
<style>
  :root {
    --yellow: #fcd533;
    --red: #e52228;
    --black: #111111;
    --white: #ffffff;
    --text: #1a1a1a;
  }
  * { margin: 0; padding: 0; box-sizing: border-box; }
  html, body { width: 849px; height: 1200px; overflow: hidden; background: var(--white); }
  .flyer { position: relative; width: 849px; height: 1200px; overflow: hidden; font-family: "Roboto", sans-serif; color: var(--text); }

  .hero-photo {
    position: absolute; left: 0; top: 0; width: 849px; height: 549px;
    background: linear-gradient(100deg, #f4f5f6 0%, #e4e6e8 28%, #b9a89a 48%, #8b7f72 56%, #2e3238 68%, #5a5f66 80%, #c9ccd0 100%);
  }

  .brand-box {
    position: absolute; left: 0; top: 0; width: 418px; height: 178px; background: var(--white);
    display: flex; flex-direction: column; justify-content: center; padding-left: 78px;
  }
  .brand-row { display: flex; align-items: center; gap: 12px; }
  .brand-mark { width: 30px; height: 30px; background: var(--red); }
  .brand-name { font-family: "Archivo Black", sans-serif; font-size: 46px; line-height: 1; color: var(--black); }
  .brand-tag { margin-top: 8px; margin-left: 46px; font-size: 12px; letter-spacing: 4px; color: #333; }

  .headline {
    position: absolute; left: 51px; top: 212px;
    font-family: "Roboto Condensed", sans-serif; font-weight: 700; color: var(--black);
    text-transform: uppercase; line-height: 1;
  }
  .headline .line { display: block; font-size: 52px; margin-bottom: 6px; }
  .headline .line-large { font-size: 92px; margin: 0; line-height: 0.9; }

  .about { position: absolute; left: 40px; top: 578px; width: 380px; font-size: 19.5px; line-height: 24.3px; white-space: nowrap; }
  .about h2 { font-size: 24px; line-height: 28px; font-weight: 700; margin-bottom: 32px; }
  .about p { margin-bottom: 24.3px; }
  .about p.tight { margin-bottom: 0; }
  .about strong { font-weight: 900; }

  .services-panel {
    position: absolute; left: 424px; top: 467px; width: 373px; height: 622px; background: var(--yellow);
    padding: 19px 0 0 24px;
  }
  .services-title { font-family: "Roboto", sans-serif; font-weight: 900; color: var(--red); font-size: 28px; line-height: 40px; margin-left: 5px; text-transform: uppercase; }
  .services-list { list-style: none; margin-top: 13px; font-weight: 900; font-size: 25px; line-height: 35.5px; color: var(--black); text-transform: uppercase; }
  .services-list li::before { content: "> "; }
  .new-heading { margin-top: 25px; font-weight: 900; font-size: 25px; line-height: 30px; text-transform: uppercase; color: var(--black); }
  .new-list { list-style: none; margin-top: 1px; font-size: 26px; line-height: 32px; text-transform: uppercase; color: var(--black); }

  .van-photo {
    position: absolute; left: 444px; top: 863px; width: 332px; height: 213px;
    border: 4px solid var(--white);
    background: linear-gradient(160deg, #3f5a36 0%, #6e7f60 35%, #262626 55%, #d9d9d9 75%, #8d8d8d 100%);
  }

  .review-band {
    position: absolute; left: 0; top: 1089px; width: 849px; height: 49px; background: var(--yellow);
    display: flex; align-items: center; justify-content: center; font-size: 20.5px; color: var(--black); white-space: nowrap;
  }
  .contact-band {
    position: absolute; left: 0; top: 1138px; width: 849px; height: 62px; background: var(--red);
    display: flex; align-items: center; color: var(--white); font-weight: 700; font-size: 25px;
  }
  .contact-item { display: flex; align-items: center; gap: 8px; }
  .contact-phone { margin-left: 56px; }
  .contact-email { margin-left: 52px; }
  .contact-item svg { width: 26px; height: 26px; fill: var(--white); }
</style>
</head>
<body>
<div class="flyer">
  <div class="hero-photo" role="img" aria-label="Photo of a handyman's tool belt with a hammer beside a brick wall"></div>

  <div class="brand-box">
    <div class="brand-row">
      <span class="brand-mark"></span>
      <span class="brand-name">Brightnail</span>
    </div>
    <div class="brand-tag">HANDYMAN SERVICES</div>
  </div>

  <h1 class="headline">
    <span class="line">Call the pros</span>
    <span class="line">not the cons</span>
    <span class="line">We do it all</span>
    <span class="line line-large">Large</span>
    <span class="line">and small</span>
  </h1>

  <section class="about">
    <h2>About us</h2>
    <p><strong>Brightnail</strong> Handyman Sevices originated<br>from a family-owned and operated<br>contractor business, performing home<br>renovation and construction work in<br>the NYC area since 2004.</p>
    <p class="tight">Today, we specialize in reliable and<br>affordable Construction services for<br>residential and commercial clients. In<br>2014, we expanded to northern New<br>Jersey. In 2016, we brought quality<br>home improvement and repair services<br>to new Bucks County, PA, and nearby<br>New Jersey areas.</p>
    <p class="tight">We offer carpentry, electrical, plumb-<br>ing, renovation, remodel, cleaning<br>services and landscaping.</p>
  </section>

  <aside class="services-panel">
    <h2 class="services-title">Brightnail Handyman<br>Service</h2>
    <ul class="services-list">
      <li>&nbsp;Small repairs</li>
      <li>Remodeling</li>
      <li>General<br>contracting</li>
    </ul>
    <div class="new-heading">New offerings:</div>
    <ul class="new-list">
      <li>Thermal inspection</li>
      <li>Cleaning service</li>
    </ul>
  </aside>

  <div class="van-photo" role="img" aria-label="Photo of the company's branded service van parked on gravel"></div>

  <div class="review-band">Check out our 5-star reviews at www.brightnailhh.test| instagram: #brightnailhandyman</div>

  <div class="contact-band">
    <div class="contact-item contact-phone">
      <svg viewBox="0 0 24 24" aria-hidden="true"><path d="M6.6 10.8a15.2 15.2 0 0 0 6.6 6.6l2.2-2.2a1 1 0 0 1 1-.25 11.4 11.4 0 0 0 3.6.57 1 1 0 0 1 1 1V20a1 1 0 0 1-1 1A17 17 0 0 1 3 4a1 1 0 0 1 1-1h3.5a1 1 0 0 1 1 1c0 1.25.2 2.45.57 3.6a1 1 0 0 1-.25 1z"/></svg>
      <span>555) 014-2290</span>
    </div>
    <div class="contact-item contact-email">
      <svg viewBox="0 0 24 24" aria-hidden="true"><path d="M2 5h20v14H2z M3.5 6.5v.4L12 13l8.5-6.1v-.4z" fill-rule="evenodd"/></svg>
      <span>brightnailnyc@mailbox.test</span>
    </div>
  </div>
</div>
</body>
</html>
```